Garlic Farm for Farm Sales/Restaurant sales

Need a professional, but appealing to agriculture world. We are selling 27 kinds of Organic Garlic from a farm in Simla,CO. I have uploaded logo and business information-we are going to need a template, because I will need to use it for four separate people.
-We are trying to appeal to Farm to table restaurants
-As well as growers/farmers

Target Market(s)

Agriculture Sales/Restaurants-Organic

Industry/Entity Type

Agriculture

Contact Information for Business Card

Want it to look more unique then your average orbel mart card- I want it to look amazing

Font styles to use
Sans Serif

Colors
0455a3
ec1f27
fbed22
ffffff

Requirements
Must have
• Just be creative
Nice to have
• Colorful
Should not have
• plain

```html
<!DOCTYPE html>
<html lang="en">
<head>
<meta charset="utf-8">
<title>Summit Ridge Garlic – Business Card</title>
<link rel="stylesheet" href="https://fonts.googleapis.com/css2?family=Montserrat:wght@500;600&family=Josefin+Sans:wght@400;600&display=swap">
<style>
  :root {
    --navy: #1b2e5c;
    --red: #d8222d;
    --yellow: #f5d914;
    --white: #ffffff;
    --stage: #2a2a2c;
    --ink: #1b2e5c;
  }
  * { box-sizing: border-box; margin: 0; padding: 0; }
  html, body { width: 1200px; height: 900px; overflow: hidden; background: var(--stage); }
  .stage {
    width: 1200px; height: 900px;
    display: flex; flex-direction: column; align-items: center; justify-content: center; gap: 48px;
  }
  .card {
    position: relative; width: 640px; height: 366px; overflow: hidden;
    box-shadow: 0 10px 24px rgba(0,0,0,.45);
  }

  /* Front */
  .card-front { background: var(--navy); }
  .rule { position: absolute; height: 4px; background: var(--yellow); }
  .rule-upper { left: 420px; right: 0; top: 150px; }
  .rule-lower { left: 0; width: 280px; top: 262px; }
  .brand {
    position: absolute; left: 0; right: 0; top: 92px;
    display: flex; flex-direction: column; align-items: center; gap: 14px;
  }
  .brand-mark { width: 64px; height: 64px; border-radius: 50%; background: var(--red); }
  .brand-name {
    font-family: "Montserrat", sans-serif; font-weight: 600; font-size: 30px;
    color: var(--white); letter-spacing: .5px;
  }
  .social {
    position: absolute; left: 0; right: 0; top: 244px;
    display: flex; justify-content: center; gap: 14px; padding-left: 40px;
  }
  .social-dot { width: 22px; height: 22px; border-radius: 50%; background: var(--white); }

  /* Back */
  .card-back { background: var(--white); }
  .accent-bar { position: absolute; left: 40px; top: 0; bottom: 0; width: 16px; background: var(--red); }
  .back-brand {
    position: absolute; right: 36px; top: 30px;
    display: flex; flex-direction: column; align-items: center; gap: 8px;
  }
  .back-mark { width: 96px; height: 96px; border-radius: 50%; background: var(--red); }
  .back-name {
    font-family: "Montserrat", sans-serif; font-weight: 600; font-size: 13px; color: var(--navy);
  }
  .contact {
    position: absolute; right: 36px; top: 168px; list-style: none;
    font-family: "Josefin Sans", sans-serif; font-size: 15px; color: var(--ink);
    text-align: right; line-height: 23px;
  }
  .contact li { display: flex; justify-content: flex-end; align-items: center; gap: 8px; }
  .contact .icon { width: 14px; height: 14px; background: var(--red); display: inline-flex; align-items: center; justify-content: center; }
  .contact .icon svg { width: 10px; height: 10px; }
  .contact .spacer { width: 14px; }
  .contact .hl { color: var(--red); }
  .person {
    position: absolute; left: 78px; bottom: 30px;
    font-family: "Montserrat", sans-serif; font-weight: 600; font-size: 28px;
    letter-spacing: 1px; color: var(--navy);
  }
  .person .surname { color: var(--red); }
</style>
</head>
<body>
<main class="stage">
  <section class="card card-front" aria-label="Card front">
    <div class="rule rule-upper"></div>
    <div class="rule rule-lower"></div>
    <div class="brand">
      <span class="brand-mark"></span>
      <span class="brand-name">Summit Ridge Garlic</span>
    </div>
    <div class="social" aria-label="Social links">
      <span class="social-dot"></span><span class="social-dot"></span><span class="social-dot"></span><span class="social-dot"></span>
    </div>
  </section>

  <section class="card card-back" aria-label="Card back">
    <div class="accent-bar"></div>
    <div class="back-brand">
      <span class="back-mark"></span>
      <span class="back-name">Summit Ridge Garlic</span>
    </div>
    <ul class="contact">
      <li>P.O. Box 48 Elmore, CO 80912 <span class="spacer"></span></li>
      <li>719-555-0142
        <span class="icon"><svg viewBox="0 0 10 10"><path d="M2 1l2 2-1 1.2c.6 1.2 1.6 2.2 2.8 2.8L7 6l2 2-1.3 1.4C4.5 9.2.8 5.5.6 2.3Z" fill="#fff"/></svg></span>
      </li>
      <li>Lena@SRGarlic.com
        <span class="icon"><svg viewBox="0 0 10 10"><rect x="1" y="2.5" width="8" height="5" fill="none" stroke="#fff" stroke-width="1"/><path d="M1 2.5l4 3 4-3" fill="none" stroke="#fff" stroke-width="1"/></svg></span>
      </li>
      <li>www.<span class="hl">SRG</span>arlic.com
        <span class="icon"><svg viewBox="0 0 10 10"><circle cx="5" cy="5" r="3.6" fill="none" stroke="#fff" stroke-width="1"/><path d="M1.4 5h7.2M5 1.4c-1.6 2-1.6 5.2 0 7.2M5 1.4c1.6 2 1.6 5.2 0 7.2" fill="none" stroke="#fff" stroke-width=".8"/></svg></span>
      </li>
    </ul>
    <p class="person">LENA <span class="surname">MARSH</span></p>
  </section>
</main>
</body>
</html>
```